Introduction flyer

Bright Harvest Nutrition & Wellness Consulting, is a new holistic nutritional therapy specialising in womens health. I want a flyer that appeals to women between 15 to 60. It must speak "health, food & balance". I have attached the basic info I need included in the text. I like Greens & Blues, soft text. My flyer will be distributed to cafes, shops, fitness centres, hung up in grocery stores & health centres etc. The QERV & DLUP logos need to appear on the flyer to show I am fully registered. My own logo & company name is attached.

Target Market(s)

Women from 10 to 60 years old.

Industry/Entity Type

Nutritionist

Colors
32a6d7
abd037
33b8a4
fbf289
ffcf3e
b768aa
d5d5d5
dcdcdc
e8e8e8

Requirements
Must have
• An image of healthy food & ladies. A group of women eating soup, stews or curry type dishes, with plenty of colour - no bread or white wine, and not just fruit please. Food that looks enjoyable to the average person.
• Nutrition is main part of my job, so please keep that in mind & emphasise food & natural well being.
Should not have
• People exercising, men, white wine, bread, cakes, sweets etc..

```html
<!DOCTYPE html>
<html lang="en">
<head>
<meta charset="utf-8">
<title>Bright Harvest Nutrition – Introduction Flyer</title>
<link href="https://fonts.googleapis.com/css2?family=Cinzel:wght@400;500&family=Roboto+Slab:wght@400&family=Lato:ital,wght@0,400;0,700;1,400&family=Raleway:wght@500;700&display=swap" rel="stylesheet">
<style>
  :root{
    --blue:#3b7fc8;
    --blue-light:#6fa2dd;
    --blue-deep:#2f6db5;
    --green:#1e9a3c;
    --green-leaf:#2a9b44;
    --text:#3c3c3c;
    --muted:#555;
    --page:#ececec;
    --paper:#fbfcfd;
  }
  *{margin:0;padding:0;box-sizing:border-box}
  html,body{width:1200px;height:1200px;overflow:hidden;background:var(--page)}
  .stage{position:relative;width:1200px;height:1200px}
  .flyer{
    position:absolute;left:197px;top:30px;width:890px;height:1258px;
    transform:scale(0.906);transform-origin:0 0;
    background:var(--paper);overflow:hidden;
    box-shadow:0 6px 22px rgba(0,0,0,.18);
    font-family:'Lato',sans-serif;color:var(--text);
  }
  .art{position:absolute;left:0;top:0}
  .abs{position:absolute}
  .brand{left:520px;top:158px;width:360px;text-align:center;color:var(--blue);font-family:'Cinzel',serif;font-weight:400}
  .brand-name{font-size:20px;letter-spacing:.5px;line-height:1.1}
  .brand-sub{font-size:15px;letter-spacing:2px;line-height:1.3}
  .headline{left:52px;top:548px;width:500px}
  .hl-do{font-family:'Cinzel',serif;font-weight:500;color:var(--green);font-size:50px;line-height:1.05}
  .hl-1{font-family:'Roboto Slab',serif;color:var(--blue);font-size:26px;line-height:1.3}
  .hl-2{font-family:'Raleway',sans-serif;font-weight:700;color:var(--green);font-size:30px;line-height:1.25}
  .hl-3{font-family:'Roboto Slab',serif;color:var(--blue);font-size:25px;line-height:1.25}
  .visit-text{left:545px;top:500px;width:276px;text-align:center;color:#fff;font-family:'Raleway',sans-serif;font-weight:500;font-size:22px;line-height:27px}
  .tagline{left:54px;top:752px;font-family:'Roboto Slab',serif;color:var(--green);font-size:18.5px}
  .motto{left:54px;top:782px;font-size:22px;color:var(--text)}
  .intro{left:54px;top:816px;width:790px;font-size:12.6px;line-height:16.4px;color:var(--text)}
  .services{left:53px;top:905px;width:440px}
  .services h2{font-family:'Lato',sans-serif;font-weight:700;color:var(--green);font-size:17.5px;line-height:22px;margin-bottom:18px}
  .services ul{list-style:none}
  .services li{position:relative;padding-left:22px;font-size:13px;line-height:16px;margin-bottom:5px;color:var(--text)}
  .services li::before{content:"»";position:absolute;left:0;top:-3px;color:var(--blue);font-weight:700;font-size:18px}
  .divider{left:501px;top:930px;width:1px;height:276px;background:var(--blue-light)}
  .contact{left:535px;top:902px;width:318px;text-align:center}
  .call{font-family:'Cinzel',serif;color:var(--blue);font-size:20.5px;letter-spacing:.3px}
  .phone{font-size:22px;color:var(--text);margin-top:2px}
  .email{font-size:16px;color:var(--text);margin-top:2px}
  .icon{display:block;margin:6px auto 0}
  .book{font-family:'Cinzel',serif;color:var(--green);font-size:17px;line-height:21px;margin-top:20px;letter-spacing:.3px}
  .note{margin-top:20px;font-style:italic;font-size:12px;line-height:16.3px;text-align:justify;text-align-last:center;color:var(--text);padding-left:16px}
</style>
</head>
<body>
<div class="stage">
  <div class="flyer">
    <svg class="art" width="890" height="1258" viewBox="0 0 890 1258" aria-hidden="false">
      <defs>
        <linearGradient id="photoTone" x1="0" y1="0" x2="1" y2="1">
          <stop offset="0" stop-color="#dfe9f2"/>
          <stop offset=".55" stop-color="#eef3f7"/>
          <stop offset="1" stop-color="#f6f1ee"/>
        </linearGradient>
      </defs>
      <!-- photo area -->
      <path role="img" aria-label="Photo: smiling group of women sharing colourful healthy dishes" d="M0 0 H600 C640 160 630 380 600 520 C400 505 170 430 0 270 Z" fill="url(#photoTone)"/>
      <!-- corners -->
      <path d="M0 0 H52 C30 14 10 34 0 62 Z" fill="var(--blue)"/>
      <path d="M818 0 H890 V72 C868 38 846 14 818 0 Z" fill="var(--green-leaf)"/>
      <!-- blue swoosh -->
      <path d="M0 262 C160 420 380 495 560 520 L560 562 C360 540 150 470 0 420 Z" fill="var(--blue)"/>
      <path d="M0 300 C170 440 390 510 560 532 L560 546 C380 528 160 462 0 345 Z" fill="var(--blue-light)"/>
      <!-- green leaf -->
      <path d="M890 225 C860 330 800 420 735 470 C800 445 850 435 890 440 Z" fill="var(--green-leaf)"/>
      <path d="M890 395 C840 420 790 460 760 500 C810 475 860 468 890 470 Z" fill="#4cb35e"/>
      <!-- ribbon under badge -->
      <path d="M800 620 C835 650 852 690 848 730 C835 700 815 670 790 650 Z" fill="var(--blue-deep)"/>
      <!-- home visits badge -->
      <circle cx="683" cy="590" r="140" fill="var(--blue)"/>
      <circle cx="683" cy="590" r="130" fill="none" stroke="#fff" stroke-width="1.5" stroke-dasharray="5 4"/>
      <!-- logo placeholder -->
      <circle cx="700" cy="102" r="12" fill="var(--green-leaf)"/>
      <!-- registration badges -->
      <rect role="img" aria-label="Registration badge" x="610" y="224" width="82" height="28" rx="4" fill="#e4e0ec"/>
      <rect role="img" aria-label="Registration badge" x="716" y="220" width="72" height="36" rx="4" fill="#e0efe3"/>
      <!-- bottom band -->
      <rect x="0" y="1232" width="890" height="26" fill="var(--blue)"/>
    </svg>

    <div class="abs brand">
      <div class="brand-name">BRIGHT HARVEST NUTRITION</div>
      <div class="brand-sub">&amp; Wellness Consulting</div>
    </div>

    <div class="abs visit-text">HOME VISITS<br>available,<br>AT NO EXTRA COST<br>within local area;<br>I can visit<br>your place of work<br>OR HOME.</div>

    <div class="abs headline">
      <div class="hl-do">Do you</div>
      <div class="hl-1">experience low energy, low libido,</div>
      <div class="hl-2">menstrual cycle complications</div>
      <div class="hl-3">OR ARE YOU PLANNING A BABY?</div>
    </div>

    <div class="abs tagline">Small changes to your diet may lead to big changes in your health.</div>
    <div class="abs motto">Eat well, live well.</div>
    <p class="abs intro">Discover exactly what YOU need to change and how to make these changes long lasting. There is no 1 rule-fits-all. My nutritional advice aims to dig up the root cause to my client's health concerns. My lifestyle plans are completely personalised to an individual's needs and circumstances. I consider the whole person not just symptoms or disease.</p>

    <section class="abs services">
      <h2>Qualified, Registered and fully insured Nutritional Therapist &amp; Wellness Consultant, specialising in:</h2>
      <ul>
        <li>Fertility, IVF, pre-conception, pregnancy &amp; post-natal care</li>
        <li>Menstrual cycle challenges<br>(PCOS, Endometriosis, PMS, heavy/irregular periods etc)</li>
        <li>Thyroid conditions</li>
        <li>Low libido</li>
        <li>Digestive health</li>
        <li>Chronic fatigue syndrome</li>
        <li>Perimenopause/menopause</li>
        <li>Weight management</li>
        <li>Type 2 diabetes, blood sugar dysregulation, high blood pressure, high cholesterol</li>
        <li>Recurring infections e.g. thrush, UTIs, coughs, colds</li>
      </ul>
    </section>

    <div class="abs divider"></div>

    <section class="abs contact">
      <div class="call">CALL MAEVE TODAY ON</div>
      <svg class="icon" width="18" height="18" viewBox="0 0 24 24"><path d="M6.6 10.8a15 15 0 0 0 6.6 6.6l2.2-2.2c.3-.3.7-.4 1-.2 1.1.4 2.3.6 3.6.6.6 0 1 .4 1 1V20c0 .6-.4 1-1 1A17 17 0 0 1 3 4c0-.6.4-1 1-1h3.5c.6 0 1 .4 1 1 0 1.2.2 2.4.6 3.6.1.3 0 .7-.2 1z" fill="var(--blue)"/></svg>
      <div class="phone">085-0000-142</div>
      <svg class="icon" width="20" height="16" viewBox="0 0 20 16"><rect x="1" y="2" width="18" height="12" rx="1.5" fill="var(--blue)"/><path d="M1.5 3 L10 9.5 L18.5 3" fill="none" stroke="#fff" stroke-width="1.4"/></svg>
      <div class="email">maeve@brightharvestnutrition.ie</div>
      <div class="book">TO BOOK A CONSULTATION OR<br>FOR A FREE NO OBLIGATION<br>15-minute MINI CONSULTATION</div>
      <p class="note">Initial consultations typically last up to 2 hours, follow-ups 30 – 60 minutes. Further investigative tests may be recommended such as blood, urine, saliva sampling. These will always be agreed with the client in advance.</p>
    </section>
  </div>
</div>
</body>
</html>
```